Flyer Design Project for our Parenting Psychologists at the Wellmind Counselling Centre

At the Wellmind Counselling Centre we have expert Parenting Psychologists.

Parenting Psychologists provide practical, step by step assistance to parents who are struggling with their children's behavioural and emotional problems.

We need a DL size brochure that will be appealing to parents. The brochure will be on show in schools, kindergartens and GP clinics.

In terms of style it will be in line with our website and stationery that I will attach.

www.wellmindcounsellingcentre.com.au

Hi Everyone,
Thanks for putting forward your proposals, there are a couple there that I am very interested in. I am looking to see if there is a way that I can change my brief to guaranteed as I am definitely going to be using one of the designs for sure.
I have emailed ArtForge and as soon as I get an answer I will change it if I can.
If anyone out there already knows the answer please let me know :-)
Thanks,
Marcie.

Hi Again,

I worked it out myself!!

I have now changed this to a committed project.

Kind regards,
Marcie.

Reason: I have 46 designs now and need more time to work out which is best!

Target Market(s)

The target will be educated professional parents motivated to get professional help. And doctors and teachers who will pass on the brochures 2 parents

Industry/Entity Type

Health

Requirements
Must have
• I want one DL size brochure. Back and front.

We need text (below) and our contact details. Our logo.

6352 1840
Suite 1, 2087 Tamworth Rd, Tamworth North 3118

Text:
Parents want the best for their kids. They want kids that are happy, healthy and well behaved.

So why is it so hard? Parents of toddlers, primary schoolers and teenagers alike say that they are frustrated by constant nagging, bribing and yelling, they don't know what to try next. Some parents worry that their children are unhappy. Struggling at school, not making friends or coping with bigger problems.

The good news is that getting your children to behave more co-operatively doesn't need to be difficult or mysterious. We all know that kids don't come with manuals, but there are skills every parent can learn to make parenting easier. In a few sessions with a Parenting Psychologist, you will receive step by step guidance in how to talk to your children in a way that will be much more effective getting them to behave in a respectful and co-operative way around the home and in public. You will learn how to help your child cope with problems they are going through. They can help you reconnect with your kids so you can enjoy being a parent again.

Nice to have
• Themes consistent with our website
and letterhead, business cards. I will attach these.
Should not have
• I don't want it to look too cluttered so if the text I have provided up above looks too crowded then I will edit it.

```html
<!DOCTYPE html>
<html lang="en">
<head>
<meta charset="utf-8">
<title>Wellmind Counselling Centre – Parenting DL Flyer</title>
<link href="https://fonts.googleapis.com/css2?family=Baloo+2:wght@800&family=Didact+Gothic&display=swap" rel="stylesheet">
<style>
  :root {
    --page-bg: #e6e6e6;
    --panel-cream: #efe5d7;
    --panel-light: #f6f1ea;
    --heading-green: #648a5c;
    --text-dark: #1f1f1f;
    --logo-grey: #6c6c6c;
    --logo-teal: #8cc9c8;
    --stripe-green: #6a9a6a;
    --stripe-aqua: #88c1c3;
    --stripe-teal: #6f9e9e;
    --stripe-slate: #737c80;
    --stripe-deep: #3e6e68;
    --stripe-charcoal: #3c3a36;
    --stripe-olive: #9a9466;
  }
  * { box-sizing: border-box; margin: 0; padding: 0; }
  html, body { width: 1200px; height: 900px; overflow: hidden; }
  body {
    background: var(--page-bg);
    font-family: "Didact Gothic", "Helvetica Neue", Arial, sans-serif;
    position: relative;
  }
  .panel {
    position: absolute;
    top: 53px;
    width: 371px;
    height: 791px;
    background: var(--panel-cream);
    overflow: hidden;
  }
  .panel--front { left: 173px; }
  .panel--back { left: 656px; }

  .stripe-band { position: absolute; left: 0; right: 0; display: flex; }
  .stripe-band span { flex: 1; }
  .stripe-band--top { top: 0; height: 35px; }
  .stripe-band--bottom { bottom: 0; height: 14px; }
  .stripe-band--top .s1 { background: var(--stripe-green); }
  .stripe-band--top .s2 { background: var(--stripe-aqua); }
  .stripe-band--top .s3 { background: var(--stripe-teal); }
  .stripe-band--top .s4 { background: var(--stripe-slate); }
  .stripe-band--bottom .s1 { background: var(--stripe-deep); }
  .stripe-band--bottom .s2 { background: var(--stripe-aqua); }
  .stripe-band--bottom .s3 { background: var(--stripe-charcoal); }
  .stripe-band--bottom .s4 { background: var(--stripe-olive); }

  .hero-photo {
    position: absolute;
    top: 35px; left: 0;
    width: 371px; height: 320px;
    background: linear-gradient(135deg, #f4f2f0 0%, #e9d6cc 35%, #d8b7a3 55%, #f1ece8 100%);
  }
  .hero-curve { position: absolute; top: 290px; left: 0; width: 371px; height: 70px; }

  .front-heading {
    position: absolute;
    top: 386px; left: 0; right: 0;
    text-align: center;
    font-family: "Baloo 2", "Arial Rounded MT Bold", sans-serif;
    font-weight: 800;
    font-size: 45px;
    line-height: 50px;
    color: var(--heading-green);
  }
  .front-sub {
    position: absolute;
    top: 559px; left: 0; right: 0;
    text-align: center;
    font-size: 21px;
    line-height: 29px;
    color: var(--text-dark);
  }

  .brand {
    position: absolute;
    display: flex;
    align-items: center;
    gap: 34px;
  }
  .brand__dot {
    width: 60px; height: 60px;
    border-radius: 50%;
    background: var(--logo-teal);
    flex-shrink: 0;
  }
  .brand__name {
    font-size: 20px;
    line-height: 25px;
    letter-spacing: 3px;
    text-transform: uppercase;
    color: var(--logo-grey);
  }
  .panel--front .brand { top: 655px; left: 57px; }

  .back-heading {
    position: absolute;
    top: 52px; left: 20px; right: 20px;
    text-align: center;
    font-family: "Baloo 2", "Arial Rounded MT Bold", sans-serif;
    font-weight: 800;
    font-size: 23px;
    line-height: 27px;
    color: var(--heading-green);
  }
  .back-body {
    position: absolute;
    top: 136px; left: 20px; right: 18px;
    font-size: 13.6px;
    line-height: 18.3px;
    text-align: justify;
    color: var(--text-dark);
  }
  .back-body p + p { margin-top: 18.3px; }

  .brand-strip {
    position: absolute;
    top: 547px; left: 0; right: 0;
    height: 126px;
    background: var(--panel-light);
  }
  .panel--back .brand { top: 571px; left: 57px; }

  .contact {
    position: absolute;
    top: 684px; left: 0; right: 0;
    text-align: center;
    font-size: 14px;
    line-height: 19.5px;
    font-style: normal;
    color: var(--text-dark);
  }
  .contact__web { font-weight: 700; font-family: Arial, sans-serif; font-size: 13.5px; }
</style>
</head>
<body>

  <section class="panel panel--front">
    <div class="stripe-band stripe-band--top"><span class="s1"></span><span class="s2"></span><span class="s3"></span><span class="s4"></span></div>

    <div class="hero-photo" role="img" aria-label="Photo of a mother comforting her crying young daughter"></div>
    <svg class="hero-curve" viewBox="0 0 371 70" preserveAspectRatio="none" aria-hidden="true">
      <path d="M0,42 Q150,-6 371,38 L371,70 L0,70 Z" fill="#ffffff" opacity="0.55"/>
      <path d="M0,48 Q160,4 371,52 L371,70 L0,70 Z" fill="var(--panel-cream)"/>
    </svg>

    <h1 class="front-heading">Parents want<br>the best for<br>their kids.</h1>
    <p class="front-sub">They want kids that are happy,<br>healthy and well behaved.</p>

    <div class="brand">
      <span class="brand__dot"></span>
      <span class="brand__name">Wellmind<br>Counselling<br>Centre</span>
    </div>

    <div class="stripe-band stripe-band--bottom"><span class="s1"></span><span class="s2"></span><span class="s3"></span><span class="s4"></span></div>
  </section>

  <section class="panel panel--back">
    <div class="stripe-band stripe-band--top"><span class="s1"></span><span class="s2"></span><span class="s3"></span><span class="s4"></span></div>

    <h2 class="back-heading">Parents want the best for<br>their kids.</h2>

    <div class="back-body">
      <p>So why is it so hard? Parents of toddlers, primary schoolers and teenagers alike say that they are frustrated by constant nagging, bribing and yelling, they don't know what to try next. Some parents worry that their children are unhappy. Struggling at school, not making friends or coping with bigger problems.</p>
      <p>The good news is that getting your children to behave more co-operatively doesn't need to be difficult or mysterious. We all know that kids don't come with manuals, but there are skills every parent can learn to make parenting easier. In a few sessions with a Parenting Psychologist, you will receive step by step guidance in how to talk to your children in a way that will be much more effective getting them to behave in a respectful and co-operative way around the home and in public. You will learn how to help your child cope with problems they are going through. They can help you reconnect with your kids so you can enjoy being a parent again.</p>
    </div>

    <div class="brand-strip"></div>
    <div class="brand">
      <span class="brand__dot"></span>
      <span class="brand__name">Wellmind<br>Counselling<br>Centre</span>
    </div>

    <address class="contact">
      6352 1840<br>
      Suite 1, 2087 Tamworth Rd,<br>
      Tamworth North 3118<br>
      <span class="contact__web">www.wellmindcounsellingcentre.com.au</span>
    </address>

    <div class="stripe-band stripe-band--bottom"><span class="s1"></span><span class="s2"></span><span class="s3"></span><span class="s4"></span></div>
  </section>

</body>
</html>
```